Booklet Menu Design for Saffron Terrace – Chantilly, VA

Design Preferences:

Elegant and modern design with soft pastel tones

Should reflect a Mediterranean touch through subtle design elements or colors

Our food is Halal, which should be noted in a minimal and elegant way

Operating hours: 7 days a week, 11 AM – 8 PM

The final design should feel refined, welcoming, and easy to read

Materials Provided:

Full menu items (Excel file)

Multiple versions of our logo (in different formats)

We want a professional, visually appealing menu that highlights our Mediterranean cuisine while maintaining a clean and elegant aesthetic.

Restaurant address: 2715 Willowmere Commons Dr #3B Chantilly, VA 20151
Restaurant phone: (571) 555-0143
Website: www.saffronterrace.us

```html
<!DOCTYPE html>
<html lang="en">
<head>
<meta charset="utf-8">
<title>Saffron Terrace – Menu</title>
<link href="https://fonts.googleapis.com/css2?family=Open+Sans:wdth,wght@75..100,400..800&family=Roboto+Condensed:wght@500;700;900&display=swap" rel="stylesheet">
<style>
:root{
  --orange:#e4572e;
  --cream:#f3efe4;
  --paper:#f6f3ea;
  --ink:#1b1b1b;
  --rule:#3a3a3a;
  --halal:#3aa04a;
  --stage:#e6e6e6;
}
*{box-sizing:border-box;margin:0;padding:0}
html,body{width:1061px;height:1200px;overflow:hidden}
body{background:var(--stage);font-family:"Open Sans",sans-serif;color:var(--ink)}
.spread{position:absolute;left:120px;top:24px;display:grid;grid-template-columns:400px 400px;grid-template-rows:566px 566px;gap:20px}
.page{position:relative;background:var(--paper);box-shadow:0 2px 8px rgba(0,0,0,.25);overflow:hidden}

/* side band */
.band{position:absolute;left:12px;top:0;bottom:0;width:74px;background:var(--orange)}
.band::before,.band::after{content:"";position:absolute;top:0;bottom:0;width:1.5px;background:var(--cream)}
.band::before{left:5px}
.band::after{right:5px}
.band-notch{position:absolute;left:0;width:74px;height:60px}
.band-notch.top{top:0}
.band-notch.bottom{bottom:0}
.band-name{position:absolute;left:50%;top:50%;transform:translate(-50%,-50%) rotate(-90deg);white-space:nowrap;display:flex;align-items:center;gap:10px;
  font-family:"Roboto Condensed",sans-serif;font-weight:700;font-size:19px;letter-spacing:1px;color:var(--cream)}
.band-dot{width:14px;height:14px;border-radius:50%;background:var(--cream)}

/* menu content */
.menu{position:absolute;left:86px;right:22px;top:30px}
.section-title{border:1px solid var(--rule);border-top:none;text-align:center;font-family:"Roboto Condensed",sans-serif;font-weight:700;
  font-size:13px;color:var(--orange);letter-spacing:.4px;padding:3px 0 2px;margin-bottom:6px;border-left:none;border-right:1px solid var(--rule);
  border-top:1px solid var(--rule)}
.items{list-style:none;padding:0 12px 0 18px;margin-bottom:6px}
.item{display:flex;align-items:baseline;font-stretch:75%;font-weight:600;font-size:10.5px;line-height:15px}
.item .leader{flex:1;border-bottom:1px dotted #9a9a9a;margin:0 4px;transform:translateY(-3px)}

/* contact box */
.contact{position:absolute;left:86px;right:22px;bottom:34px;height:88px;background:#ebe6d8;border:1px solid #b7b2a4;
  display:flex;flex-direction:column;align-items:center;justify-content:center;gap:4px;font-stretch:75%;font-size:10px;font-weight:500}
.contact svg{display:block;margin:0 auto 1px}
.contact p{text-align:center}

/* cover */
.cover-frame{position:absolute;inset:10px;border:3px solid var(--orange);outline:1.5px solid var(--ink);outline-offset:-7px}
.cover-photo{position:absolute;left:16px;right:16px;top:250px;bottom:40px;
  background:radial-gradient(ellipse at 40% 60%,rgba(120,110,95,.35),rgba(200,192,178,.15) 60%,transparent 80%)}
.cover-mark{position:absolute;left:50%;top:48px;transform:translateX(-50%);width:92px;height:92px;border-radius:50%;background:var(--orange)}
.halal-seal{position:absolute;right:36px;top:140px;width:40px;height:40px;border-radius:50%;background:var(--halal);border:2px solid #fff;box-shadow:0 0 0 1.5px var(--halal)}
.cover-name{position:absolute;left:0;right:0;top:158px;text-align:center;font-family:"Roboto Condensed",sans-serif;font-weight:700;
  font-size:44px;line-height:42px;color:var(--orange);letter-spacing:1.5px}
.cover-menu{position:absolute;left:0;right:0;top:272px;text-align:center;font-family:"Roboto Condensed",sans-serif;font-weight:900;font-size:44px;letter-spacing:1px}
.hours{position:absolute;left:50%;top:350px;transform:translateX(-50%);background:#fff;border:1.5px solid var(--ink);padding:4px 12px 3px;text-align:center;
  font-weight:600;font-size:18px;line-height:20px;white-space:nowrap}
.hours .time{color:var(--orange)}
.cover-web{position:absolute;left:0;right:0;bottom:30px;text-align:center;font-size:10px;letter-spacing:1.5px;font-weight:500}
</style>
</head>
<body>
<main class="spread">

  <!-- page: pizza / drinks / dessert -->
  <section class="page">
    <div class="band">
      <svg class="band-notch top" viewBox="0 0 74 60"><polygon points="0,0 18,0 18,0 0,60" fill="var(--paper)"/><polygon points="74,0 56,0 74,60" fill="var(--paper)"/></svg>
      <svg class="band-notch bottom" viewBox="0 0 74 60"><polygon points="0,60 18,60 0,0" fill="var(--paper)"/><polygon points="74,60 56,60 74,0" fill="var(--paper)"/></svg>
      <div class="band-name">SAFFRON<span class="band-dot"></span>TERRACE</div>
    </div>
    <div class="menu">
      <h2 class="section-title">PIZZA</h2>
      <ul class="items">
        <li class="item"><span>Cheese Pizza</span><span class="leader"></span><span>$11.99</span></li>
        <li class="item"><span>Doner Pizza</span><span class="leader"></span><span>$17.99</span></li>
        <li class="item"><span>Chicken Doner Pizza</span><span class="leader"></span><span>$15.99</span></li>
        <li class="item"><span>Pastrami Pizza</span><span class="leader"></span><span>$17.99</span></li>
        <li class="item"><span>Sucuk&amp;Pastrami Pizza</span><span class="leader"></span><span>$19.99</span></li>
        <li class="item"><span>Veggie Pizza</span><span class="leader"></span><span>$14.99</span></li>
        <li class="item"><span>Zaatar&amp;Cheese Pizza</span><span class="leader"></span><span>$14.99</span></li>
      </ul>
      <h2 class="section-title">DRINKS</h2>
      <ul class="items">
        <li class="item"><span>Bottle Soda</span><span class="leader"></span><span>$2.99</span></li>
        <li class="item"><span>Ayran (Yogurt Drink)</span><span class="leader"></span><span>$3.99</span></li>
        <li class="item"><span>Salgam (Turnip Juice)</span><span class="leader"></span><span>$2.99</span></li>
        <li class="item"><span>Water</span><span class="leader"></span><span>$1.99</span></li>
        <li class="item"><span>Citrus Gazoz Drink</span><span class="leader"></span><span>$2.99</span></li>
        <li class="item"><span>Can Soda</span><span class="leader"></span><span>$2.99</span></li>
      </ul>
      <h2 class="section-title">DESSERT</h2>
      <ul class="items">
        <li class="item"><span>Havuc Baklava (1 Piece)</span><span class="leader"></span><span>$7.99</span></li>
        <li class="item"><span>Baklava (1 Piece)</span><span class="leader"></span><span>$2.49</span></li>
        <li class="item"><span>Kadayif (1 Piece)</span><span class="leader"></span><span>$2.99</span></li>
        <li class="item"><span>Kazandibi</span><span class="leader"></span><span>$7.99</span></li>
        <li class="item"><span>Firin Sutlac</span><span class="leader"></span><span>$7.99</span></li>
        <li class="item"><span>Terrace Kunefe</span><span class="leader"></span><span>$9.99</span></li>
      </ul>
    </div>
    <address class="contact">
      <p><svg width="9" height="11" viewBox="0 0 9 11"><path d="M4.5 0A4 4 0 0 0 .5 4c0 3 4 7 4 7s4-4 4-7a4 4 0 0 0-4-4z" fill="var(--orange)"/><circle cx="4.5" cy="4" r="1.5" fill="#ebe6d8"/></svg>2715 Willowmere Commons Dr #3B Chantilly, VA 20151</p>
      <p><svg width="10" height="10" viewBox="0 0 10 10"><path d="M2 0l2 2.5-1.2 1.3a6 6 0 0 0 3.4 3.4L7.5 6 10 8l-1.5 2C4 10 0 6 0 1.5z" fill="var(--orange)"/></svg>(571) 555-0143</p>
      <p><svg width="10" height="10" viewBox="0 0 10 10"><circle cx="5" cy="5" r="4.3" fill="none" stroke="var(--orange)" stroke-width="1.2"/><path d="M.7 5h8.6M5 .7c-2.4 2.6-2.4 6 0 8.6M5 .7c2.4 2.6 2.4 6 0 8.6" fill="none" stroke="var(--orange)" stroke-width="1"/></svg>www.saffronterrace.us</p>
    </address>
  </section>

  <!-- cover -->
  <section class="page cover">
    <div class="cover-photo" role="img" aria-label="Faded photograph of Mediterranean dishes and salads on dark plates"></div>
    <div class="cover-frame"></div>
    <div class="cover-mark"></div>
    <div class="halal-seal" role="img" aria-label="Halal certification seal"></div>
    <h1 class="cover-name">SAFFRON<br>TERRACE</h1>
    <p class="cover-menu">MENU</p>
    <p class="hours">7 DAYS A WEEK<br><span class="time">11 AM – 8 PM</span></p>
    <p class="cover-web">www.saffronterrace.us</p>
  </section>

  <!-- page: soup / appetizers / doner / grill -->
  <section class="page">
    <div class="band">
      <svg class="band-notch top" viewBox="0 0 74 60"><polygon points="0,0 18,0 0,60" fill="var(--paper)"/><polygon points="74,0 56,0 74,60" fill="var(--paper)"/></svg>
      <svg class="band-notch bottom" viewBox="0 0 74 60"><polygon points="0,60 18,60 0,0" fill="var(--paper)"/><polygon points="74,60 56,60 74,0" fill="var(--paper)"/></svg>
      <div class="band-name">SAFFRON<span class="band-dot"></span>TERRACE</div>
    </div>
    <div class="menu">
      <h2 class="section-title">SOUP</h2>
      <ul class="items">
        <li class="item"><span>Lentil Soup</span><span class="leader"></span><span>$7.99</span></li>
        <li class="item"><span>Kelle Paca Soup</span><span class="leader"></span><span>$9.99</span></li>
      </ul>
      <h2 class="section-title">APPETIZERS</h2>
      <ul class="items">
        <li class="item"><span>Antep Ezme</span><span class="leader"></span><span>$5.99</span></li>
        <li class="item"><span>Babaganush</span><span class="leader"></span><span>$5.99</span></li>
        <li class="item"><span>Cacik (Tzatziki)</span><span class="leader"></span><span>$5.99</span></li>
        <li class="item"><span>Chicken Nuggets</span><span class="leader"></span><span>$8.99</span></li>
        <li class="item"><span>Cig Kofte (2-4 Person)</span><span class="leader"></span><span>$12.99</span></li>
        <li class="item"><span>Falafel</span><span class="leader"></span><span>$10.99</span></li>
        <li class="item"><span>Eggplant Salad</span><span class="leader"></span><span>$5.99</span></li>
        <li class="item"><span>Hummus</span><span class="leader"></span><span>$5.99</span></li>
        <li class="item"><span>Sarma (Stuffed Leaves)</span><span class="leader"></span><span>$6.99</span></li>
        <li class="item"><span>Terrace Meze (2 Person)</span><span class="leader"></span><span>$13.99</span></li>
        <li class="item"><span>Sigara Boregi</span><span class="leader"></span><span>$6.99</span></li>
      </ul>
      <h2 class="section-title">DONER</h2>
      <ul class="items">
        <li class="item"><span>Doner w/ Rice</span><span class="leader"></span><span>$19.99</span></li>
        <li class="item"><span>Doner Iskender</span><span class="leader"></span><span>$20.99</span></li>
        <li class="item"><span>Chicken Doner w/ Rice</span><span class="leader"></span><span>$17.99</span></li>
        <li class="item"><span>Chicken Doner Iskender</span><span class="leader"></span><span>$18.99</span></li>
        <li class="item"><span>Doner 1LB</span><span class="leader"></span><span>$27.99</span></li>
        <li class="item"><span>Chicken Doner 1LB</span><span class="leader"></span><span>$24.99</span></li>
      </ul>
      <h2 class="section-title">GRILL</h2>
      <ul class="items">
        <li class="item"><span>Adana Kebab w/ Rice</span><span class="leader"></span><span>$19.99</span></li>
        <li class="item"><span>Beyti Kebab</span><span class="leader"></span><span>$23.99</span></li>
        <li class="item"><span>Kofte w/ Rice</span><span class="leader"></span><span>$19.99</span></li>
        <li class="item"><span>Chicken Shish w/ Rice</span><span class="leader"></span><span>$19.99</span></li>
        <li class="item"><span>Lamb Chops w/ Rice</span><span class="leader"></span><span>$27.99</span></li>
        <li class="item"><span>Mixed Grill Kebab</span><span class="leader"></span><span>$27.99</span></li>
        <li class="item"><span>Lamb Shish w/ Rice</span><span class="leader"></span><span>$27.99</span></li>
      </ul>
    </div>
  </section>

  <!-- page: sides / chef specials / sandwich & wrap / pide -->
  <section class="page">
    <div class="band">
      <svg class="band-notch top" viewBox="0 0 74 60"><polygon points="0,0 18,0 0,60" fill="var(--paper)"/><polygon points="74,0 56,0 74,60" fill="var(--paper)"/></svg>
      <svg class="band-notch bottom" viewBox="0 0 74 60"><polygon points="0,60 18,60 0,0" fill="var(--paper)"/><polygon points="74,60 56,60 74,0" fill="var(--paper)"/></svg>
      <div class="band-name">SAFFRON<span class="band-dot"></span>TERRACE</div>
    </div>
    <div class="menu">
      <h2 class="section-title">SIDES</h2>
      <ul class="items">
        <li class="item"><span>French Fries</span><span class="leader"></span><span>$4.99</span></li>
        <li class="item"><span>Rice</span><span class="leader"></span><span>$4.99</span></li>
        <li class="item"><span>Lavash Bread</span><span class="leader"></span><span>$2.49</span></li>
      </ul>
      <h2 class="section-title">CHEF SPECIALS</h2>
      <ul class="items">
        <li class="item"><span>Terrace Burger</span><span class="leader"></span><span>$19.99</span></li>
        <li class="item"><span>Terrace Duo Grill</span><span class="leader"></span><span>$59.99</span></li>
        <li class="item"><span>Terrace Trio Grill</span><span class="leader"></span><span>$89.99</span></li>
        <li class="item"><span>Lamb Shank</span><span class="leader"></span><span>$21.99</span></li>
        <li class="item"><span>Kuru Fasulye</span><span class="leader"></span><span>$16.99</span></li>
        <li class="item"><span>Kavurma</span><span class="leader"></span><span>$19.99</span></li>
      </ul>
      <h2 class="section-title">SANDWICH &amp; WRAP</h2>
      <ul class="items">
        <li class="item"><span>Doner Wrap</span><span class="leader"></span><span>$15.49</span></li>
        <li class="item"><span>Doner Sandwich</span><span class="leader"></span><span>$15.49</span></li>
        <li class="item"><span>Adana Kebab Wrap</span><span class="leader"></span><span>$15.49</span></li>
        <li class="item"><span>Adana Kebab Sandwich</span><span class="leader"></span><span>$15.49</span></li>
        <li class="item"><span>Chicken Doner Wrap</span><span class="leader"></span><span>$15.49</span></li>
        <li class="item"><span>Chicken Doner Swich</span><span class="leader"></span><span>$15.49</span></li>
        <li class="item"><span>Kofte Sandwich</span><span class="leader"></span><span>$15.49</span></li>
        <li class="item"><span>Chicken Shish Sandwich</span><span class="leader"></span><span>$15.49</span></li>
      </ul>
      <h2 class="section-title">SANDWICH &amp; WRAP</h2>
      <ul class="items">
        <li class="item"><span>Lahmacun</span><span class="leader"></span><span>$9.99</span></li>
        <li class="item"><span>Terrace Pide</span><span class="leader"></span><span>$17.99</span></li>
        <li class="item"><span>Kusbasili Pide</span><span class="leader"></span><span>$15.99</span></li>
        <li class="item"><span>Kiymali Pide</span><span class="leader"></span><span>$14.99</span></li>
        <li class="item"><span>Sucuk Pide</span><span class="leader"></span><span>$15.99</span></li>
        <li class="item"><span>Cheese Pide</span><span class="leader"></span><span>$13.99</span></li>
        <li class="item"><span>Zaatar</span><span class="leader"></span><span>$7.99</span></li>
      </ul>
    </div>
  </section>

</main>
</body>
</html>
```